HR Technology Company (Corvexa) needs a consistent powerpoint deck for future presentations

We are Corvexa (corvexa-example.com). You can visit our website for colours scheme etc. I am looking for a full PPT pack which can be used for various presentations in the future. Sales Presentation, Company Overview etc. This must include charts, graphs, services (4/6/8 items), people slide, timeline slides etc among all the other common slides.

```html
<!DOCTYPE html>
<html lang="en">
<head>
<meta charset="utf-8">
<title>Corvexa Presentation Deck</title>
<link href="https://fonts.googleapis.com/css2?family=Poppins:ital,wght@0,400;0,500;0,600;0,700;1,700&display=swap" rel="stylesheet">
<style>
  :root {
    --canvas: #74b0e0;
    --slide: #ffffff;
    --orange: #f28c28;
    --brown: #8b4513;
    --ink: #1d1d35;
    --navy: #1b2a78;
    --deep: #0d1a5a;
    --grey-dark: #3a3a3c;
    --green: #8cc63f;
    --blue: #3b7fc4;
    --teal: #5fc2a8;
    --pale-blue: #cfe6f7;
    --frame: #3a2e6e;
  }
  html, body { margin: 0; padding: 0; width: 1200px; height: 1200px; overflow: hidden; }
  body { background: var(--canvas); position: relative; font-family: "Poppins", sans-serif; }
  .slide { position: absolute; width: 367px; height: 206px; background: var(--slide); display: block; }
  .slide--cover { left: 29px; top: 129px; background: var(--grey-dark); }
  .slide--timeline { left: 416px; top: 129px; }
  .slide--chart { left: 800px; top: 129px; }
  .slide--market { left: 32px; top: 367px; }
  .slide--people { left: 416px; top: 367px; }
  .slide--pillars { left: 800px; top: 367px; }
  .slide--stack { left: 32px; top: 615px; }
  .slide--stats { left: 416px; top: 615px; }
  .slide--overview { left: 800px; top: 615px; }
  .slide--list { left: 416px; top: 839px; }
  svg text { font-family: "Poppins", sans-serif; }
  .title { fill: var(--orange); font-size: 13px; font-weight: 500; }
  .small { fill: var(--ink); font-size: 5px; }
  .tiny { fill: var(--ink); font-size: 4px; }
  .body { fill: var(--ink); font-size: 6.5px; }
  .pill { fill: var(--grey-dark); }
  .pill-text { fill: #fff; font-size: 5px; }
  .heading-italic { fill: var(--orange); font-size: 10px; font-weight: 700; font-style: italic; }
  .navy-label { fill: var(--navy); font-size: 8px; font-weight: 600; }
  .rule { stroke: var(--ink); stroke-width: 1; fill: none; }
</style>
</head>
<body>

<!-- Cover -->
<svg class="slide slide--cover" viewBox="0 0 459 258">
  <defs>
    <linearGradient id="cubeFill" x1="0" y1="0" x2="1" y2="1">
      <stop offset="0" stop-color="#2b2b2d"/><stop offset="1" stop-color="#444446"/>
    </linearGradient>
  </defs>
  <rect x="200" y="0" width="259" height="190" fill="url(#cubeFill)" role="img" aria-label="Scattered black isometric cubes decoration"/>
  <polygon points="0,258 459,258 459,205 0,235" fill="#2a2a2b"/>
  <rect x="28" y="84" width="8" height="8" fill="var(--orange)"/>
  <text x="40" y="92" fill="#fff" font-size="13" font-weight="500">Corvexa</text>
  <text x="28" y="154" fill="#fff" font-size="28" font-weight="500">LOREM</text>
  <text x="28" y="180" fill="#fff" font-size="18" font-weight="500">IPSUM</text>
</svg>

<!-- Timeline -->
<svg class="slide slide--timeline" viewBox="0 0 459 258">
  <text class="title" x="19" y="29">Lorem Ipsum</text>
  <path d="M30,104 C40,150 100,150 120,140 C140,130 150,95 189,104 C228,113 230,150 258,140 C286,130 290,95 327,104 C364,113 370,150 396,140 C420,130 425,110 430,104" stroke="#222" stroke-width="14" fill="none"/>
  <path d="M30,104 C40,150 100,150 120,140" stroke="var(--orange)" stroke-width="5" fill="none"/>
  <path d="M189,104 C228,113 230,150 258,140" stroke="var(--orange)" stroke-width="5" fill="none"/>
  <path d="M327,104 C364,113 370,150 396,140" stroke="var(--orange)" stroke-width="5" fill="none"/>
  <g fill="#fff" stroke="var(--orange)" stroke-width="2">
    <circle cx="51" cy="104" r="21"/><circle cx="120" cy="140" r="21"/><circle cx="189" cy="104" r="21"/>
    <circle cx="258" cy="140" r="21"/><circle cx="327" cy="104" r="21"/><circle cx="396" cy="140" r="21"/>
  </g>
  <g fill="none" stroke="var(--orange)" stroke-width="1.5">
    <circle cx="51" cy="104" r="9"/><circle cx="51" cy="104" r="5"/><circle cx="51" cy="104" r="1.5"/>
    <path d="M112,146 l8,-10 l8,10 z"/>
    <path d="M181,96 l16,16 M197,96 l-16,16"/>
    <circle cx="258" cy="140" r="9"/><path d="M249,140 h18 M258,131 v18"/>
    <path d="M319,112 v-14 M319,112 h16 M322,110 v-5 M327,110 v-8 M332,110 v-11"/>
    <path d="M389,147 l10,-14 l5,-3 l-2,6 l-10,14 z"/>
  </g>
  <g text-anchor="middle">
    <text class="small" x="120" y="55">Lorem ipsum is simply</text><text class="small" x="120" y="62">dummy industry.</text>
    <rect class="pill" x="105" y="81" width="30" height="8" rx="4"/><text class="pill-text" x="120" y="87">2013</text>
    <text class="small" x="260" y="55">Lorem ipsum is simply</text><text class="small" x="260" y="62">dummy industry.</text>
    <rect class="pill" x="245" y="81" width="30" height="8" rx="4"/><text class="pill-text" x="260" y="87">2019</text>
    <text class="small" x="396" y="55">Lorem ipsum is simply</text><text class="small" x="396" y="62">dummy industry.</text>
    <rect class="pill" x="381" y="81" width="30" height="8" rx="4"/><text class="pill-text" x="396" y="87">2021</text>
    <text class="small" x="50" y="163">Lorem ipsum is simply</text><text class="small" x="50" y="170">dummy industry.</text>
    <rect class="pill" x="35" y="186" width="30" height="8" rx="4"/><text class="pill-text" x="50" y="192">2010</text>
    <text class="small" x="188" y="163">Lorem ipsum is simply</text><text class="small" x="188" y="170">dummy industry.</text>
    <rect class="pill" x="173" y="186" width="30" height="8" rx="4"/><text class="pill-text" x="188" y="192">2016</text>
    <text class="small" x="327" y="163">Lorem ipsum is simply</text><text class="small" x="327" y="170">dummy industry.</text>
    <rect class="pill" x="312" y="184" width="30" height="8" rx="4"/><text class="pill-text" x="327" y="190">2020</text>
  </g>
</svg>

<!-- Bar chart -->
<svg class="slide slide--chart" viewBox="0 0 459 258">
  <defs>
    <linearGradient id="barFill" x1="0" y1="0" x2="0" y2="1">
      <stop offset="0" stop-color="#b6d732"/><stop offset="0.5" stop-color="#2fa6a0"/><stop offset="1" stop-color="#2e4fb0"/>
    </linearGradient>
    <linearGradient id="legendBlue" x1="0" x2="1"><stop offset="0" stop-color="#6cc1b8"/><stop offset="1" stop-color="#2b86d0"/></linearGradient>
  </defs>
  <text class="title" x="19" y="29">Lorem Ipsum</text>
  <rect x="22" y="45" width="415" height="192" fill="none" stroke="var(--frame)" stroke-width="1"/>
  <g stroke="#9a9a9a" stroke-width="0.6">
    <line x1="45" y1="60" x2="412" y2="60"/><line x1="45" y1="87" x2="412" y2="87"/>
    <line x1="45" y1="114" x2="412" y2="114"/><line x1="45" y1="142" x2="412" y2="142"/>
    <line x1="45" y1="170" x2="412" y2="170"/>
  </g>
  <line x1="45" y1="197" x2="412" y2="197" stroke="#333" stroke-width="2"/>
  <g fill="url(#barFill)">
    <rect x="100" y="189" width="12" height="8"/><rect x="149" y="177" width="12" height="20"/>
    <rect x="199" y="181" width="12" height="16"/><rect x="248" y="175" width="12" height="22"/>
    <rect x="297" y="165" width="12" height="32"/><rect x="346" y="67" width="12" height="130"/>
  </g>
  <g text-anchor="middle" class="tiny">
    <text class="tiny" x="106" y="209">Q3-2021</text><text class="tiny" x="155" y="209">Q4-2021</text>
    <text class="tiny" x="205" y="209">Q1-2022</text><text class="tiny" x="254" y="209">Q2-2022</text>
    <text class="tiny" x="303" y="209">Q3-2022</text><text class="tiny" x="352" y="209">Q4-2022</text>
  </g>
  <rect x="99" y="220" width="36" height="8" fill="#b6d732"/><text class="tiny" x="137" y="226">Lorem Ipsum</text>
  <rect x="207" y="220" width="36" height="8" fill="url(#legendBlue)"/><text class="tiny" x="245" y="226">Lorem Ipsum</text>
  <rect x="308" y="220" width="36" height="8" fill="#6a3ea1"/><text class="tiny" x="346" y="226">Lorem Ipsum</text>
</svg>

<!-- Market size -->
<svg class="slide slide--market" viewBox="0 0 459 258">
  <text class="title" x="19" y="29">Lorem Ipsum</text>
  <circle cx="133" cy="136" r="90" fill="var(--deep)"/>
  <circle cx="133" cy="150" r="76" fill="#132a7c"/>
  <circle cx="133" cy="162" r="63" fill="#1f3f9f"/>
  <circle cx="133" cy="184" r="41" fill="var(--green)"/>
  <text x="133" y="239" text-anchor="middle" fill="var(--ink)" font-size="8">Relative size not to scale</text>
  <g stroke="var(--navy)" stroke-width="0.8">
    <line x1="210" y1="87" x2="286" y2="87"/><line x1="222" y1="122" x2="286" y2="122"/>
    <line x1="222" y1="157" x2="286" y2="157"/>
  </g>
  <line x1="172" y1="193" x2="286" y2="193" stroke="var(--green)" stroke-width="0.8"/>
  <g fill="var(--navy)">
    <polygon points="286,85 290,87 286,89"/><polygon points="286,120 290,122 286,124"/><polygon points="286,155 290,157 286,159"/>
  </g>
  <polygon points="286,191 290,193 286,195" fill="var(--green)"/>
  <text class="navy-label" x="306" y="87">TAM</text>
  <text class="tiny" x="306" y="94">Macro Dev Market ~45M growing</text><text class="tiny" x="306" y="100">20% annually</text>
  <text class="navy-label" x="306" y="124">Stackra TAM</text>
  <text class="tiny" x="306" y="131">Stackra Addressable Market</text>
  <text class="navy-label" x="306" y="160">Stackra Users</text>
  <text class="navy-label" x="306" y="196">Target</text>
  <text class="tiny" x="306" y="203">Companies with &gt;250 employees</text>
</svg>

<!-- People -->
<svg class="slide slide--people" viewBox="0 0 459 258">
  <text class="title" x="19" y="29">Lorem Ipsum</text>
  <rect x="24" y="45" width="411" height="172" fill="none" stroke="#555" stroke-width="0.8"/>
  <g fill="var(--grey-dark)" stroke="#fff" stroke-width="2">
    <circle cx="229" cy="47" r="15"/>
    <circle cx="73" cy="104" r="14"/><circle cx="151" cy="104" r="14"/><circle cx="229" cy="104" r="14"/><circle cx="307" cy="104" r="14"/><circle cx="386" cy="104" r="14"/>
    <circle cx="73" cy="166" r="14"/><circle cx="151" cy="166" r="14"/><circle cx="229" cy="166" r="14"/><circle cx="307" cy="166" r="14"/><circle cx="386" cy="166" r="14"/>
  </g>
  <g fill="none" stroke="#666" stroke-width="0.6" stroke-dasharray="1.5 1.5">
    <circle cx="229" cy="47" r="18"/>
    <circle cx="73" cy="104" r="17"/><circle cx="151" cy="104" r="17"/><circle cx="229" cy="104" r="17"/><circle cx="307" cy="104" r="17"/><circle cx="386" cy="104" r="17"/>
    <circle cx="73" cy="166" r="17"/><circle cx="151" cy="166" r="17"/><circle cx="229" cy="166" r="17"/><circle cx="307" cy="166" r="17"/><circle cx="386" cy="166" r="17"/>
  </g>
  <g text-anchor="middle">
    <text class="tiny" x="229" y="71">Lorem Ipsum</text><text class="tiny" x="229" y="76">CEO</text>
    <text class="tiny" x="73" y="130">Lorem Ipsum</text><text class="tiny" x="73" y="135">CFO</text>
    <text class="tiny" x="151" y="130">Lorem Ipsum</text><text class="tiny" x="151" y="135">General Counsel</text>
    <text class="tiny" x="229" y="130">Dana Moreno</text><text class="tiny" x="229" y="135">SVP, Sales</text>
    <text class="tiny" x="307" y="130">Lorem Ipsum</text><text class="tiny" x="307" y="135">Management</text>
    <text class="tiny" x="386" y="130">Lorem Ipsum</text><text class="tiny" x="386" y="135">VP, Marketing</text>
    <text class="tiny" x="73" y="192">Lorem Ipsum</text><text class="tiny" x="73" y="197">CTO</text>
    <text class="tiny" x="151" y="192">Lorem Ipsum</text><text class="tiny" x="151" y="197">VP, Engineering</text>
    <text class="tiny" x="229" y="192">Lorem Ipsum</text><text class="tiny" x="229" y="197">Head of Design</text>
    <text class="tiny" x="307" y="192">Lorem Ipsum</text><text class="tiny" x="307" y="197">Supply Chain</text>
    <text class="tiny" x="386" y="192">Lorem Ipsum</text><text class="tiny" x="386" y="197">VP, People</text>
  </g>
  <g fill="var(--navy)" font-size="6.5" font-weight="500">
    <text x="24" y="233">Remote-First</text><text x="24" y="242">Jan 31st end of Fiscal Year</text>
    <text x="229" y="233" text-anchor="middle">120-ish Employees</text>
    <text x="435" y="233" text-anchor="end">50% International</text>
  </g>
</svg>

<!-- Vision / Mission / Virtues / Strategy -->
<svg class="slide slide--pillars" viewBox="0 0 459 258">
  <defs><marker id="arrowInk" markerWidth="6" markerHeight="6" refX="5" refY="3" orient="auto"><path d="M0,0 L6,3 L0,6 z" fill="var(--ink)"/></marker></defs>
  <text class="title" x="19" y="29">Lorem Ipsum</text>
  <g class="rule" marker-end="url(#arrowInk)">
    <path d="M28,63 h-7 v142 q0,5 5,5 h76"/><path d="M134,63 h-7 v142 q0,5 5,5 h76"/>
    <path d="M240,63 h-7 v142 q0,5 5,5 h76"/><path d="M346,63 h-7 v142 q0,5 5,5 h76"/>
  </g>
  <text class="heading-italic" x="32" y="66">VISION</text>
  <text class="heading-italic" x="138" y="66">MISSION</text>
  <text class="heading-italic" x="244" y="66">VIRTUES</text>
  <text class="heading-italic" x="350" y="66">STRATEGY</text>
  <g fill="var(--ink)" font-size="8.5">
    <text x="32" y="87">Lorem Ipsum</text><text x="138" y="87">Lorem Ipsum</text>
    <text x="244" y="87">Lorem Ipsum</text><text x="350" y="87">Lorem Ipsum</text>
  </g>
  <g class="small">
    <text class="small" x="32" y="112">Lorem Ipsum is</text><text class="small" x="32" y="120">simply dummy text of</text>
    <text class="small" x="32" y="128">the printing and</text><text class="small" x="32" y="136">typesetting industry.</text>
    <text class="small" x="138" y="112">Lorem Ipsum is</text><text class="small" x="138" y="120">simply dummy</text>
    <text class="small" x="138" y="128">text of the printing</text><text class="small" x="138" y="136">and typesetting</text>
    <text class="small" x="138" y="144">industry.</text>
  </g>
  <g fill="var(--orange)">
    <circle cx="233" cy="110" r="2"/><circle cx="233" cy="128" r="2"/><circle cx="233" cy="147" r="2"/><circle cx="233" cy="165" r="2"/>
    <circle cx="339" cy="110" r="2"/><circle cx="339" cy="128" r="2"/><circle cx="339" cy="147" r="2"/><circle cx="339" cy="165" r="2"/>
  </g>
  <g>
    <text class="small" x="244" y="112">Lorem Ipsum</text><text class="small" x="244" y="130">Lorem Ipsum</text>
    <text class="small" x="244" y="149">Lorem Ipsum</text><text class="small" x="244" y="167">Lorem Ipsum</text>
    <text class="small" x="350" y="112">Lorem Ipsum</text><text class="small" x="350" y="130">Lorem Ipsum</text>
    <text class="small" x="350" y="149">Lorem Ipsum</text><text class="small" x="350" y="167">Lorem Ipsum</text>
  </g>
</svg>

<!-- Container stack -->
<svg class="slide slide--stack" viewBox="0 0 459 258">
  <text class="title" x="19" y="29">Lorem Ipsum</text>
  <rect x="20" y="42" width="225" height="188" rx="5" fill="#fff" stroke="#444" stroke-width="0.8"/>
  <text x="132" y="54" text-anchor="middle" fill="var(--ink)" font-size="6.5">Containerized Applications</text>
  <rect x="27" y="68" width="210" height="6" fill="var(--pale-blue)"/>
  <g fill="var(--blue)">
    <rect x="27" y="79" width="32" height="71"/><rect x="62" y="79" width="32" height="71"/><rect x="98" y="79" width="32" height="71"/>
    <rect x="133" y="79" width="32" height="71"/><rect x="169" y="79" width="32" height="71"/><rect x="204" y="79" width="33" height="71"/>
  </g>
  <g fill="#fff" font-size="6" text-anchor="middle">
    <text transform="translate(45 114) rotate(-90)">App A</text><text transform="translate(80 114) rotate(-90)">App B</text>
    <text transform="translate(116 114) rotate(-90)">App C</text><text transform="translate(151 114) rotate(-90)">App D</text>
    <text transform="translate(187 114) rotate(-90)">App E</text><text transform="translate(222 114) rotate(-90)">App F</text>
  </g>
  <rect x="27" y="153" width="210" height="20" fill="var(--blue)"/>
  <text x="132" y="165" text-anchor="middle" fill="#fff" font-size="6.5">Stackra</text>
  <rect x="27" y="177" width="210" height="20" fill="var(--pale-blue)"/>
  <text x="132" y="190" text-anchor="middle" fill="var(--ink)" font-size="6.5">Host Operating System</text>
  <rect x="27" y="201" width="210" height="21" fill="var(--teal)"/>
  <text x="132" y="214" text-anchor="middle" fill="#fff" font-size="6.5">Infrastructure</text>
  <g>
    <text class="small" x="259" y="52">Lorem Ipsum is simply dummy text of the</text>
    <text class="small" x="259" y="61">printing and typesetting industry. Lorem</text>
    <text class="small" x="259" y="70">Ipsum has been the industry's standard</text>
    <text class="small" x="259" y="79">dummy text ever since the 1500s, when an</text>
    <text class="small" x="259" y="88">unknown printer took a galley of type and</text>
    <text class="small" x="259" y="97">scrambled it to make a type specimen book.</text>
  </g>
  <text x="259" y="124" fill="var(--orange)" font-size="11">Benefits:</text>
  <g fill="var(--orange)">
    <circle cx="262" cy="144" r="2"/><circle cx="262" cy="162" r="2"/><circle cx="262" cy="181" r="2"/><circle cx="262" cy="199" r="2"/><circle cx="262" cy="217" r="2"/>
  </g>
  <g>
    <text class="small" x="269" y="146">Lorem Ipsum</text><text class="small" x="269" y="164">Lorem Ipsum</text>
    <text class="small" x="269" y="183">Lorem Ipsum</text><text class="small" x="269" y="201">Lorem Ipsum</text>
    <text class="small" x="269" y="219">Lorem Ipsum</text>
  </g>
</svg>

<!-- Key figures -->
<svg class="slide slide--stats" viewBox="0 0 459 258">
  <text class="title" x="19" y="29">Lorem Ipsum</text>
  <line x1="20" y1="116" x2="435" y2="116" stroke="var(--ink)" stroke-width="1"/>
  <g fill="none" stroke="#555" stroke-width="0.8">
    <path d="M40,116 a28,28 0 0 1 56,0"/><path d="M120,116 a28,28 0 0 0 56,0"/>
    <path d="M199,116 a28,28 0 0 1 56,0"/><path d="M278,116 a28,28 0 0 0 56,0"/>
    <path d="M358,116 a28,28 0 0 1 56,0"/>
  </g>
  <circle cx="68" cy="116" r="24" fill="var(--orange)"/>
  <circle cx="148" cy="116" r="24" fill="var(--brown)"/>
  <circle cx="227" cy="116" r="24" fill="var(--orange)"/>
  <circle cx="306" cy="116" r="24" fill="var(--brown)"/>
  <circle cx="386" cy="116" r="24" fill="var(--orange)"/>
  <g fill="none" stroke="#fff" stroke-width="1.2">
    <path d="M60,110 h16 l4,4 -12,10 -12,-10 z"/>
    <path d="M148,124 l-9,-9 a5,5 0 0 1 9,-5 a5,5 0 0 1 9,5 z"/>
    <rect x="218" y="109" width="18" height="14" rx="2"/><path d="M225,113 l-2,3 2,3 M229,113 l2,3 -2,3"/>
    <path d="M298,110 h6 l2,2 h8 v12 h-16 z"/>
    <path d="M378,118 a5,5 0 0 1 3,-9 a6,6 0 0 1 11,2 a4,4 0 0 1 0,8 z M386,116 v9 M383,122 l3,3 3,-3"/>
  </g>
  <g text-anchor="middle" fill="var(--ink)" font-size="7">
    <text x="68" y="165">#1</text><text x="68" y="174">Lorem Ipsum</text>
    <text x="148" y="165">#2</text><text x="148" y="174">Lorem Ipsum</text>
    <text x="227" y="165">13M+</text><text x="227" y="174">Lorem Ipsum</text>
    <text x="306" y="165">7M+</text><text x="306" y="174">Lorem Ipsum</text>
    <text x="386" y="165">13B+</text><text x="386" y="174">Lorem Ipsum</text>
  </g>
</svg>

<!-- Overview with illustration -->
<svg class="slide slide--overview" viewBox="0 0 459 258">
  <defs>
    <marker id="arrowInk2" markerWidth="6" markerHeight="6" refX="5" refY="3" orient="auto"><path d="M0,0 L6,3 L0,6 z" fill="var(--ink)"/></marker>
    <linearGradient id="dashboardArt" x1="0" y1="0" x2="1" y2="1"><stop offset="0" stop-color="#2f5fc0"/><stop offset="1" stop-color="#dfe8f7"/></linearGradient>
  </defs>
  <text class="title" x="19" y="29">Lorem Ipsum</text>
  <g class="rule" marker-end="url(#arrowInk2)">
    <path d="M28,44 h-7 v83 h244"/><path d="M28,147 h-7 v80 h244"/>
  </g>
  <text x="32" y="54" fill="var(--ink)" font-size="13">Lorem Ipsum</text>
  <g>
    <text class="small" x="32" y="71">Lorem Ipsum is simply dummy text of the printing and</text>
    <text class="small" x="32" y="80">typesetting industry. Lorem Ipsum has been the industry's</text>
    <text class="small" x="32" y="89">standard dummy text ever since the 1500s, when an</text>
    <text class="small" x="32" y="98">unknown printer took a galley of type and scrambled it to</text>
    <text class="small" x="32" y="107">make a type specimen book.</text>
  </g>
  <text x="32" y="157" fill="var(--ink)" font-size="13">Lorem Ipsum</text>
  <g>
    <text class="small" x="32" y="174">Lorem Ipsum is simply dummy text of the printing and</text>
    <text class="small" x="32" y="183">typesetting industry. Lorem Ipsum has been the industry's</text>
    <text class="small" x="32" y="192">standard dummy text ever since the 1500s, when an</text>
    <text class="small" x="32" y="201">unknown printer took a galley of type and scrambled it to</text>
    <text class="small" x="32" y="210">make a type specimen book.</text>
  </g>
  <rect x="278" y="88" width="165" height="145" rx="6" fill="url(#dashboardArt)" role="img" aria-label="Illustration of an analyst standing in front of large data dashboards"/>
</svg>

<!-- Bullet list with illustration -->
<svg class="slide slide--list" viewBox="0 0 459 258">
  <defs>
    <marker id="arrowInk3" markerWidth="6" markerHeight="6" refX="5" refY="3" orient="auto"><path d="M0,0 L6,3 L0,6 z" fill="var(--ink)"/></marker>
    <linearGradient id="serverArt" x1="0" y1="0" x2="1" y2="1"><stop offset="0" stop-color="#a9c8ef"/><stop offset="1" stop-color="#e6eef9"/></linearGradient>
  </defs>
  <text class="title" x="19" y="29">Lorem Ipsum</text>
  <path class="rule" d="M21,48 v167 h112" marker-end="url(#arrowInk3)"/>
  <g fill="var(--ink)">
    <circle cx="21" cy="51" r="2"/><circle cx="21" cy="69" r="2"/><circle cx="21" cy="88" r="2"/>
    <circle cx="21" cy="106" r="2"/><circle cx="21" cy="124" r="2"/><circle cx="21" cy="142" r="2"/>
    <circle cx="21" cy="161" r="2"/><circle cx="21" cy="179" r="2"/><circle cx="21" cy="197" r="2"/>
  </g>
  <g>
    <text class="small" x="32" y="53">Lorem Ipsum</text><text class="small" x="32" y="71">Lorem Ipsum</text>
    <text class="small" x="32" y="90">Lorem Ipsum</text><text class="small" x="32" y="108">Lorem Ipsum</text>
    <text class="small" x="32" y="126">Lorem Ipsum</text><text class="small" x="32" y="144">Lorem Ipsum</text>
    <text class="small" x="32" y="163">Lorem Ipsum</text><text class="small" x="32" y="181">Lorem Ipsum</text>
    <text class="small" x="32" y="199">Lorem Ipsum</text>
  </g>
  <rect x="203" y="70" width="240" height="165" rx="6" fill="url(#serverArt)" role="img" aria-label="Illustration of server racks beside a laptop showing analytics charts"/>
</svg>

</body>
</html>
```